Silver Heron Construction Services

Create a business card for my business consulting company
Danielle Vesk, Founder and CEO
4816 Alder Brook Way, Ste 100
Denver, CO. 80451
303.782.4190 cell
dvesk@silverheronconst.example
www.silverheronconst.example

Target Market(s)

Private Equity and Construction Companies

Industry/Entity Type

Business / Sales Consulting

Contact Information for Business Card

Tag Line that says "Where The Road To Success Is Always Under Construction"

Requirements
Must have
• Logo on both sides of the card.
Nice to have
• Add tagline to the same side of the card as my name and contact info

```html
<!DOCTYPE html>
<html lang="en">
<head>
<meta charset="utf-8">
<title>Silver Heron Construction Services – Business Card</title>
<link href="https://fonts.googleapis.com/css2?family=Lato:wght@400;700;900&display=swap" rel="stylesheet">
<style>
  :root {
    --backdrop: #d3d6d8;
    --paper: #f1f0ee;
    --ink: #111111;
    --ink-soft: #3a3a3a;
    --rule: #1a1a1a;
  }
  * { box-sizing: border-box; margin: 0; padding: 0; }
  html, body {
    width: 1200px; height: 929px; overflow: hidden;
    background: var(--backdrop);
    font-family: "Lato", sans-serif;
    color: var(--ink);
  }
  .sheet {
    width: 1200px; height: 929px;
    display: flex; flex-direction: column;
    align-items: center; justify-content: center; gap: 56px;
  }
  .card {
    position: relative;
    width: 620px; height: 354px;
    background: var(--paper);
    box-shadow: 0 14px 30px rgba(0,0,0,0.14);
  }
  /* Front */
  .brand-name {
    font-weight: 900;
    text-transform: uppercase;
    color: var(--ink);
    line-height: 1.1;
    text-align: center;
  }
  .card-front .brand-name {
    position: absolute; left: 40px; top: 92px; width: 270px;
    font-size: 24px; letter-spacing: 0.5px;
  }
  .tagline {
    position: absolute; left: 40px; bottom: 44px;
    font-size: 15px; font-weight: 700; color: var(--ink);
  }
  .contact-block {
    position: absolute; left: 340px; top: 70px; width: 260px;
  }
  .person-name {
    font-size: 25px; font-weight: 900; text-transform: uppercase; letter-spacing: 0.3px;
  }
  .person-title {
    font-size: 16px; color: var(--ink-soft); margin-top: 2px;
  }
  .title-rule {
    width: 64px; height: 2px; background: var(--rule); margin: 10px 0 14px;
  }
  .contact-list { list-style: none; }
  .contact-list li {
    display: flex; align-items: flex-start; gap: 9px;
    font-size: 13px; line-height: 1.4; color: var(--ink-soft);
    margin-bottom: 5px;
  }
  .contact-list svg { flex: 0 0 12px; width: 12px; height: 12px; margin-top: 3px; fill: var(--ink); }
  /* Back */
  .card-back { display: flex; align-items: center; justify-content: center; }
  .card-back .brand-name { font-size: 30px; letter-spacing: 0.8px; }
</style>
</head>
<body>
<main class="sheet">
  <section class="card card-front" aria-label="Card front">
    <div class="brand-name">Silver Heron<br>Construction Services</div>
    <div class="contact-block">
      <h1 class="person-name">Danielle Vesk</h1>
      <p class="person-title">Founder &amp; CEO</p>
      <div class="title-rule"></div>
      <ul class="contact-list">
        <li>
          <svg viewBox="0 0 12 12" aria-hidden="true"><path d="M6 0a4 4 0 0 0-4 4c0 3 4 8 4 8s4-5 4-8a4 4 0 0 0-4-4zm0 5.5A1.5 1.5 0 1 1 6 2.5a1.5 1.5 0 0 1 0 3z"/></svg>
          <span>4816 Alder Brook Way, Ste 100<br>Denver, CO. 80451</span>
        </li>
        <li>
          <svg viewBox="0 0 12 12" aria-hidden="true"><path d="M3 0h6a1 1 0 0 1 1 1v10a1 1 0 0 1-1 1H3a1 1 0 0 1-1-1V1a1 1 0 0 1 1-1zm0 1.5v8h6v-8zM5.3 10.3h1.4v.8H5.3z"/></svg>
          <span>303.782.4190</span>
        </li>
        <li>
          <svg viewBox="0 0 12 12" aria-hidden="true"><path d="M0 2h12v1L6 7 0 3zm0 2.3 6 4 6-4V10H0z"/></svg>
          <span>dvesk@silverheronconst.example</span>
        </li>
        <li>
          <svg viewBox="0 0 12 12" aria-hidden="true"><path d="M6 0a6 6 0 1 0 0 12A6 6 0 0 0 6 0zm0 1.2c.8 0 1.6 1.9 1.7 4.2H4.3C4.4 3.1 5.2 1.2 6 1.2zM4.3 6.6h3.4C7.6 8.9 6.8 10.8 6 10.8s-1.6-1.9-1.7-4.2z"/></svg>
          <span>www.silverheronconst.example</span>
        </li>
      </ul>
    </div>
    <p class="tagline">The Road To Success Is Always Under Construction</p>
  </section>

  <section class="card card-back" aria-label="Card back">
    <div class="brand-name">Silver Heron<br>Construction Services</div>
  </section>
</main>
</body>
</html>
```